kVista Corporate Website

kVista is a well-funded start up developing an Online Marketing Platform for small businesses in Europe.
We are launching in February 2012 with all-in-one online marketing services including professional website, DIY SEO, Dashboard with Reports and Online marketing tools, and Support.
Our internal web designer has come up with a preliminary website design which we wish to continue to improve using new ideas, colours, layout, image, etc.
The brief is very simple - improve the website whether it is look & feel, ease of use, conversion rate - we are looking for overall improvements.
The contest will last 5 days and we will award the winner £300.
If you are the winner , you will also be required to provide designs for 3 more internal pages adhering to the proposed home page design.
Judging criteria : -
Visual Design
Layout must adhere to best practices and wire frame. If you decide to move elements around significantly please provide reason
Functional, informative and drives calls to action
Industry/Entity Type
Marketing
Look and feel
Each slider illustrates characteristics of the customer's brand and the style your logo design should communicate.

```html
<!DOCTYPE html>
<html lang="en">
<head>
<meta charset="utf-8">
<title>kVista – Online Marketing for Small Business</title>
<link href="https://fonts.googleapis.com/css2?family=Open+Sans:wght@300;400;600;700&family=Oswald:wght@500;700&display=swap" rel="stylesheet">
<style>
:root{
  --orange:#f7931e;
  --orange-dark:#e07c0c;
  --green:#5fa81c;
  --green-dark:#3f7f10;
  --grey-band:#e6e6e6;
  --panel:#ececec;
  --text:#555;
  --heading:#333;
  --footer:#262626;
  --footer-line:#3a3a3a;
  --white:#fff;
}
*{box-sizing:border-box;margin:0;padding:0}
html,body{width:743px;height:1200px;overflow:hidden}
body{position:relative;background:#f4f4f4;font-family:"Open Sans",Arial,sans-serif;color:var(--text)}
.abs{position:absolute}

.topbar{left:0;top:0;width:743px;height:30px;background:linear-gradient(#fff,#ececec)}
.nav{right:20px;top:8px;display:flex;align-items:center;font-size:7px;color:#444}
.nav a{color:#444;text-decoration:none;padding:3px 7px}
.nav span{color:#888}
.nav a.active{background:var(--orange);color:#fff;border-radius:3px}

.hero{left:0;top:30px;width:743px;height:322px;background:radial-gradient(circle at 480px 200px,#ffab3a,var(--orange) 60%)}
.logo-box{left:106px;top:0;width:180px;height:106px;background:linear-gradient(#fff,#ededed);box-shadow:0 2px 4px rgba(0,0,0,.2);display:flex;align-items:center;justify-content:center;gap:8px}
.logo-dot{width:30px;height:30px;border-radius:50%;background:var(--orange)}
.logo-name{font-size:31px;color:#222;font-weight:400}

.headline{left:102px;top:117px;font-size:18.5px;font-weight:700;color:#fff;line-height:21px;text-shadow:0 1px 2px rgba(0,0,0,.2)}
.bullets{left:102px;top:179px;list-style:none}
.bullets li{font-size:12px;font-weight:700;color:#fff;height:21px;display:flex;align-items:center;gap:12px}
.bullets svg{width:16px;height:10px}
.cta{left:216px;top:278px;width:144px;height:49px;border-radius:6px;background:linear-gradient(#7fd12b,var(--green-dark));border:2px solid #9ee05a;text-align:center;color:#fff}
.cta small{display:block;font-size:11px;margin-top:4px}
.cta strong{display:block;font-size:21px;font-weight:700;line-height:22px}

.figure{left:424px;top:112px;width:170px;height:232px;border-radius:80px 80px 20px 20px;background:linear-gradient(#c9a58c,#2c2c2c 55%)}
.bubble{background:#f8f2e6;border:1px solid #e6d6b8;font-size:6.5px;font-weight:700;color:#555;padding:3px 8px;white-space:nowrap}

.grey-band{left:0;top:352px;width:743px;height:185px;background:var(--grey-band)}
.tiles-box{left:93px;top:353px;width:557px;height:110px;background:#fff}
.tile{top:378px;width:128px;height:58px;border:1px solid #f0b86a;border-radius:3px;background:#fff;padding:8px 6px 0 35px}
.tile h3{font-size:11.5px;font-weight:400;color:var(--orange)}
.tile p{font-size:6px;line-height:8px;color:#666;margin-top:2px}
.tile svg{position:absolute;left:6px;top:14px;width:24px;height:24px}

.ribbon-tail{top:472px;width:60px;height:70px}
.ribbon{left:86px;top:464px;width:572px;height:69px;background:linear-gradient(#6cb823,var(--green));border-top:2px dashed #a6d86e;border-bottom:2px dashed #a6d86e;text-align:center;color:#fff}
.ribbon h2{font-size:17px;font-weight:300;margin-top:16px;line-height:20px}
.ribbon h2 b{font-weight:400}
.ribbon p{font-size:12px;font-weight:300;line-height:15px}

.about{left:104px;top:558px;width:536px}
.about h2{font-size:16px;font-weight:400;color:var(--heading);margin-bottom:7px}
.about p{font-size:6.6px;line-height:10.4px;margin-bottom:10px}
.brand{color:var(--orange)}

.packages{left:93px;top:714px;width:557px;height:98px;background:var(--panel);border-radius:4px}
.pkg{top:720px;width:128px;height:85px;color:#fff;font-family:"Oswald",Arial,sans-serif;overflow:hidden}
.pkg .tag{position:absolute;right:-22px;top:8px;transform:rotate(45deg);background:#1d5fa8;font-size:7px;width:74px;text-align:center;padding:1px 0}
.pkg h4{font-size:16px;line-height:19px;margin:6px 0 0 8px;font-weight:700}
.pkg h4.tight{font-size:13.5px;line-height:16px;margin-top:8px}
.pkg em{display:block;font-style:normal;font-size:7px;line-height:9px;color:#ffe27a;margin:3px 0 0 8px}
.pkg .foot{position:absolute;left:0;bottom:0;width:100%;background:rgba(0,0,0,.75);font-family:"Open Sans",sans-serif;font-size:7px;line-height:9px;text-align:center;padding:3px 0}
.how{left:518px;top:725px;width:124px}
.how h4{font-family:"Oswald",sans-serif;font-size:10px;font-weight:500;color:#333}
.how p{font-size:6.4px;line-height:10.2px;margin-top:6px}

.examples{left:117px;top:864px;width:130px}
.examples h3{font-size:10px;font-weight:400;line-height:11px;color:#333}
.examples p{font-size:6.5px;line-height:10.4px;margin-top:8px;color:#777}
.examples a{display:block;margin-top:10px;margin-left:75px;font-size:6.5px;color:var(--orange);text-decoration:none}
.thumb{top:856px;height:104px;background:linear-gradient(#e9edf2,#c6ced8)}
.thumb-main{left:350px;top:851px;width:188px;height:114px;border:3px solid var(--green);background:linear-gradient(#222 0 15%,#eef0f3 15%)}

.footer{left:0;top:1020px;width:743px;height:180px;background:var(--footer);border-top:3px solid var(--orange)}
.f-logo{left:93px;top:1010px;width:104px;height:56px;background:linear-gradient(#fff,#e3e3e3);display:flex;align-items:center;justify-content:center;gap:5px}
.f-logo .logo-dot{width:20px;height:20px}
.f-logo span{font-size:18px;color:#222}
.follow{left:102px;top:1078px;font-size:10px;color:#aaa}
.social{top:1098px;width:18px;height:18px;border-radius:50%;background:#ddd}
.col{top:1040px;width:92px}
.col h5{font-size:10.5px;font-weight:400;color:#ddd;display:flex;align-items:center;gap:8px;padding-bottom:5px;border-bottom:1px solid var(--footer-line)}
.col .ic{width:20px;height:18px;background:#666;border-radius:3px}
.col ul{list-style:none;margin-top:6px}
.col li{font-size:6.5px;color:#bbb;height:17.5px;line-height:17.5px;border-bottom:1px solid var(--footer-line)}
.col li::before{content:"›";color:var(--orange);margin-right:4px}
.subscribe input{margin-top:10px;width:94px;height:14px;border:none;font-size:6px;padding:0 4px;font-family:inherit}
.subscribe .plus{position:absolute;left:94px;top:38px;width:15px;height:14px;background:var(--green);color:#fff;font-size:11px;text-align:center;line-height:14px}
.like{display:flex;gap:4px;margin-top:18px;align-items:center}
.like i{width:26px;height:11px;background:#dde3ee;display:block}
.like b{font-size:6px;font-weight:400;color:#333;background:#fff;padding:1px 3px}
.copy{left:0;top:1166px;width:743px;text-align:center;font-size:6.8px;color:#aaa}
.copy .brand{color:#4a9be0}
</style>
</head>
<body>

<header class="abs topbar"></header>
<nav class="abs nav">
  <a class="active">HOME</a><span>|</span><a>ABOUT US</a><span>|</span><a>QUICK TOUR</a><span>|</span><a>PRICING</a><span>|</span><a>CONTACT US</a><span>|</span><a>LOGIN</a>
</nav>

<section class="abs hero">
  <div class="abs figure" role="img" aria-label="Photo of a thoughtful businessman looking up at marketing ideas"></div>
  <span class="abs bubble" style="left:345px;top:50px">PPC</span>
  <span class="abs bubble" style="left:432px;top:60px">Testimonials</span>
  <span class="abs bubble" style="left:518px;top:52px">Deals</span>
  <span class="abs bubble" style="left:556px;top:64px">Hosting</span>
  <span class="abs bubble" style="left:378px;top:80px">Email Marketing</span>
  <span class="abs bubble" style="left:440px;top:88px">Images</span>
  <span class="abs bubble" style="left:500px;top:80px">SEO</span>
  <span class="abs bubble" style="left:564px;top:82px">Content Management</span>
  <span class="abs bubble" style="left:412px;top:101px">Search Ads</span>
  <span class="abs bubble" style="left:525px;top:96px">Web Design</span>
  <span class="abs bubble" style="left:364px;top:114px">Directories</span>
  <span class="abs bubble" style="left:554px;top:116px">Reporting</span>
  <span class="abs bubble" style="left:414px;top:130px">Blog / News</span>
  <span class="abs bubble" style="left:560px;top:138px">Micro Feeds</span>
  <span class="abs bubble" style="left:392px;top:156px">Social Page</span>
  <span class="abs bubble" style="left:560px;top:162px">Referals</span>
</section>

<div class="abs logo-box"><span class="logo-dot"></span><span class="logo-name">kVista</span></div>

<h1 class="abs headline">Getting a website has never<br>been so simple</h1>
<ul class="abs bullets">
  <li><svg viewBox="0 0 16 10"><path d="M0 3h9V0l7 5-7 5V7H0z" fill="#5fa81c"/></svg>Business Websites</li>
  <li><svg viewBox="0 0 16 10"><path d="M0 3h9V0l7 5-7 5V7H0z" fill="#5fa81c"/></svg>Online Marketing</li>
  <li><svg viewBox="0 0 16 10"><path d="M0 3h9V0l7 5-7 5V7H0z" fill="#5fa81c"/></svg>Dashboard Controls</li>
  <li><svg viewBox="0 0 16 10"><path d="M0 3h9V0l7 5-7 5V7H0z" fill="#5fa81c"/></svg>Full Setup &amp; Support</li>
</ul>
<a class="abs cta"><small>Sign up NOW for</small><strong>FREE!</strong></a>

<div class="abs grey-band"></div>
<div class="abs tiles-box"></div>
<article class="abs tile" style="left:98px"><svg viewBox="0 0 24 24"><path d="M2 22h20M4 21V10h4v11M10 21V4h4v17M16 21v-7h4v7" fill="#f7931e" stroke="#f7931e"/></svg><h3>Case Studies</h3><p>Read real stories about small businesses online</p></article>
<article class="abs tile" style="left:238px"><svg viewBox="0 0 24 24"><circle cx="12" cy="9" r="7" fill="none" stroke="#f7931e" stroke-width="2"/><rect x="9" y="16" width="6" height="5" fill="#f7931e"/></svg><h3>How to</h3><p>Learn from our online marketing tips for small business</p></article>
<article class="abs tile" style="left:377px"><svg viewBox="0 0 24 24"><path d="M1 3h15v10H7l-4 4v-4H1z" fill="#f7931e"/><path d="M9 9h14v9h-2v4l-4-4H9z" fill="#e07c0c"/></svg><h3>News &amp; Chatter</h3><p>Get up-to-date news and chatter about online marketing</p></article>
<article class="abs tile" style="left:517px"><svg viewBox="0 0 24 24"><circle cx="12" cy="13" r="10" fill="#f7931e"/><path d="M12 13V7M12 13h4" stroke="#fff" stroke-width="2"/></svg><h3>Demo</h3><p>Find out what kVista can do for your business.</p></article>

<svg class="abs ribbon-tail" style="left:40px" viewBox="0 0 60 70"><path d="M60 0H0l25 35L0 70h60z" fill="#3f7f10"/></svg>
<svg class="abs ribbon-tail" style="left:642px" viewBox="0 0 60 70"><path d="M0 0h60L35 35l25 35H0z" fill="#3f7f10"/></svg>
<section class="abs ribbon">
  <h2>The Complete Online Marketing Solution for <b>Small Business Websites</b></h2>
  <p>“Get a big online presence and more sales leads in 30 minutes”</p>
</section>

<section class="abs about">
  <h2>About Us</h2>
  <p><span class="brand">kVista</span> will build your business website, optimise SEO marketing and make recommendations on best practices to help you win customers. Let our team of experts design a business website for you. Choose a business website from <span class="brand">kVista's</span> broad array of fabulous, customisable business websites and our experts will have your business online in minutes. <span class="brand">kVista</span> lets you create a professional business website without the need to know how to code or programme.</p>
  <p>Your business website comes with automatic Internet marketing, marketing on the Internet is easy with <span class="brand">kVista</span>, we automatically optimise your site for SEO marketing and we can run search ad campaigns when you need them. Get a business website with online marketing now. <span class="brand">kVista</span> brings your Small Business Website to LIFE!</p>
  <p>View our example business websites above, watch the video demo to see how to make a business website or call us now and get your business marketing online today. The <span class="brand">kVista</span> website builder gives you a professional online appearance - post your own images, give customers your latest news and create customer testimonials, it's the most complete online marketing solution for your business.</p>
</section>

<div class="abs packages"></div>
<article class="abs pkg" style="left:98px;background:linear-gradient(135deg,#e8302a,#a5121a)"><span class="tag">£199 Value</span><h4>Free<br>SETUP</h4><div class="foot">WEB OFFER ONLY</div></article>
<article class="abs pkg" style="left:236px;background:linear-gradient(135deg,#f5c21b,#e0541a)"><span class="tag">£22 /month</span><h4>Pro<br>PACKAGE</h4><em>Big online presence</em><div class="foot">Bussiness Website &amp; Easy Dashboard</div></article>
<article class="abs pkg" style="left:372px;background:linear-gradient(135deg,#2d9a2d,#0f5a17)"><span class="tag">£29 /month</span><h4 class="tight">TURBO SALES<br>PRO PLUS</h4><em>More sales LEADS</em><div class="foot">Bussiness Website,<br>Easy Dashboard &amp; ppc Sales</div></article>
<aside class="abs how"><h4>How does it work?</h4><p>Neque porro quisquam est qui dolorem ipsum quia dolor vel eum iriure dolor in hendrerit in vulputate velit dou site vesse molestie consequat, vel illumsit amet, adipisci velit"</p></aside>

<section class="abs examples">
  <h3>View examples of our stunning business websites</h3>
  <p>Duis autem vel eum iriure dolor in hendrerit in vulputate velit esse molestie consequat, vel illum dolore eu feugiat nulla facilisis at vero eros et accumsan. esse molestie.</p>
  <a>▸ View more</a>
</section>
<svg class="abs" style="left:278px;top:888px" width="12" height="26" viewBox="0 0 12 26"><path d="M12 0L0 13l12 13z" fill="#999"/></svg>
<svg class="abs" style="left:602px;top:888px" width="12" height="26" viewBox="0 0 12 26"><path d="M0 0l12 13L0 26z" fill="#f7b23c"/></svg>
<div class="abs thumb" style="left:310px;width:50px" role="img" aria-label="Example business website screenshot"></div>
<div class="abs thumb" style="left:530px;width:58px;background:linear-gradient(#1f3f78,#3b6bb0)" role="img" aria-label="Example business website screenshot"></div>
<div class="abs thumb-main" role="img" aria-label="Featured sample site screenshot"></div>

<footer class="abs footer"></footer>
<div class="abs f-logo"><span class="logo-dot"></span><span>kVista</span></div>
<div class="abs follow">Follow</div>
<span class="abs social" style="left:103px"></span>
<span class="abs social" style="left:131px"></span>
<span class="abs social" style="left:160px;background:#f7931e"></span>

<div class="abs col" style="left:204px;width:126px"><h5><span class="ic" style="border-radius:50%"></span>OurServices</h5><ul><li>Search Engine Optimization (SEO)</li><li>Social Media</li><li>Web Analytics</li></ul></div>
<div class="abs col" style="left:343px"><h5><span class="ic"></span>ContactUs</h5><ul><li>Contact Us</li><li>Customer Support</li><li>Request a call back</li><li>FAQ's</li></ul></div>
<div class="abs col" style="left:447px"><h5><span class="ic"></span>Navigation</h5><ul><li>Site Map</li><li>Terms and Condition</li><li>Privacy &amp; Policy</li><li>Get in Touch</li></ul></div>
<div class="abs col subscribe" style="left:552px;width:94px"><h5><span class="ic"></span>Subscribe</h5><input type="text" placeholder="Type your email here"><span class="plus">+</span><div class="like"><i></i><b>62</b></div></div>

<p class="abs copy">Copyright © 2011 kVista Pvt. Ltd 2011 -  All rights reserved.  Managed by <span class="brand">kVista</span>  &nbsp;|&nbsp;  Admin</p>

</body>
</html>
```